Illustrate Our Process "Bright Path Method"

We need a graphic design to brand our proprietary process. We are a wealth services team that serves a group of individual and families. Most financial advisors only provide investment management. Our team implements a process that puts our clients goals and finances on a Bright Path foundation.

Please create your own graphic that will simply explain that our elevated process will take care of a client's complete financial picture and in turn put them on a Bright Path foundation.

Our process is called the "Bright Path Method" and it involves:
1) Wealth Management
2) Tax Strategy
3) Cash Management
4) Risk Management
5) Estate Strategy
6) Philanthropy
7) Value Added Services
Note: These things were uploaded in "Bright Path A"

As a person's life becomes more complex they will grow into our process which will constantly ensure their finances & goals are on a Bright Path foundation.

I uploaded pictures of our office so you can see what might go with the overall look and feel of our office if that helps.

Industry/Entity Type

Finance

Requirements
Must have
• The final design should communicate simplicity, stability, expertise and trust. We also want a final design that will quickly describe our process instead of creating confusion.
Nice to have
• We are wanting to put the final design on a canvas print on our bookshelf (which is attached) and have the ability to blow it up and put it on one of our walls.
Should not have
• Clash with the feel and decor of our office

```html
<!DOCTYPE html>
<html lang="en">
<head>
<meta charset="utf-8">
<title>Bright Path Method</title>
<link rel="stylesheet" href="https://fonts.googleapis.com/css2?family=Aldrich&family=Oswald:wght@500;600&display=swap">
<style>
  :root{
    --frame-red:#a8282a;
    --frame-dark:#7d1b1c;
    --sky-top:#1f8fd3;
    --sky-mid:#3aa6e0;
    --sky-low:#9fd3ef;
    --scene-haze:#a89c99;
    --scene-rock:#9a3424;
    --scene-deep:#6e1e14;
    --cube-face:#e9d6cc;
    --cube-top:#f6ebe4;
    --cube-side:#c9a89a;
    --icon-red:#b3312a;
    --label-ink:#2a2a2a;
    --white:#ffffff;
  }
  *{box-sizing:border-box;margin:0;padding:0}
  html,body{width:1200px;height:848px;overflow:hidden;background:var(--white)}
  .canvas{position:relative;width:1200px;height:848px;background:var(--white)}
  .poster{
    position:absolute;left:50px;top:50px;width:1100px;height:748px;
    border:9px solid var(--frame-red);overflow:hidden;
    background:linear-gradient(180deg,var(--sky-top) 0%,var(--sky-mid) 45%,var(--sky-low) 78%);
  }
  .top-band{position:absolute;left:540px;top:-9px;width:560px;height:9px;background:var(--frame-dark)}
  .scene-art{
    position:absolute;left:0;top:330px;width:1082px;height:400px;
    background:linear-gradient(180deg,rgba(168,156,153,0) 0%,var(--scene-haze) 40%,var(--scene-rock) 70%,var(--scene-deep) 100%);
  }
  .balloon-art{
    position:absolute;left:102px;top:141px;width:141px;height:259px;border-radius:70px 70px 20px 20px;
    background:linear-gradient(180deg,#b9c4c4 0%,#8fa4a6 60%,#c98a4e 100%);
  }
  .small-balloon-art{
    position:absolute;left:1007px;top:233px;width:60px;height:104px;border-radius:30px 30px 10px 10px;
    background:linear-gradient(180deg,#e34a45,#f0d8d4 70%,#6b4a2a);
  }
  .meeting-art{
    position:absolute;left:226px;top:589px;width:185px;height:141px;
    background:linear-gradient(180deg,#e8793e 0%,#f3c0a7 45%,#d98a84 100%);
  }
  .steps{position:absolute;left:0;top:0;width:1082px;height:730px}
  .step-label{
    position:absolute;transform:translateX(-50%);text-align:center;
    font-family:"Oswald",sans-serif;font-weight:500;font-size:19px;line-height:20px;
    color:var(--label-ink);
    text-shadow:0 0 3px #fff,0 0 3px #fff,0 0 4px #fff;
    white-space:nowrap;
  }
  .headline{
    position:absolute;left:52px;top:22px;
    font-family:"Aldrich",sans-serif;font-size:48px;line-height:64px;letter-spacing:1px;
    color:var(--white);text-shadow:0 0 2px #5fb7ea;
    transform:scaleX(0.8);transform-origin:left top;white-space:nowrap;
  }
  .method-title{
    position:absolute;left:454px;top:615px;
    font-family:"Oswald",sans-serif;font-weight:600;font-size:64px;line-height:70px;letter-spacing:1px;
    color:var(--white);text-shadow:2px 3px 4px rgba(60,10,5,.55);white-space:nowrap;
  }
  .bottom-band{position:absolute;left:0;bottom:0;width:100%;height:12px;background:var(--frame-red)}
</style>
</head>
<body>
<div class="canvas">
  <div class="poster">
    <div class="top-band"></div>

    <div class="scene-art" role="img" aria-label="Desert landscape with distant hills and a large red sandstone mesa rising to the right, with sun rays and a sweeping arrow"></div>
    <div class="balloon-art" role="img" aria-label="Hot air balloon labelled wealth carrying passengers"></div>
    <div class="small-balloon-art" role="img" aria-label="Small striped hot air balloon rising above the mesa"></div>
    <div class="meeting-art" role="img" aria-label="Advisor and client meeting at a table under an orange canopy"></div>

    <svg class="steps" viewBox="0 0 1082 730" aria-hidden="true">
      <defs>
        <symbol id="cube" viewBox="0 0 64 64">
          <path d="M0 8 L8 0 L64 0 L56 8Z" fill="#f6ebe4"/>
          <path d="M56 8 L64 0 L64 56 L56 64Z" fill="#c9a89a"/>
          <rect x="0" y="8" width="56" height="56" fill="#e9d6cc"/>
        </symbol>
      </defs>
      <g stroke="#ffffff" stroke-width="1.6">
        <line x1="464" y1="326" x2="464" y2="603"/>
        <line x1="557" y1="296" x2="557" y2="548"/>
        <line x1="649" y1="254" x2="649" y2="442"/>
        <line x1="743" y1="232" x2="743" y2="434"/>
        <line x1="836" y1="180" x2="836" y2="427"/>
        <line x1="927" y1="126" x2="927" y2="427"/>
        <line x1="1017" y1="107" x2="1017" y2="236"/>
      </g>
      <g fill="#ffffff"><circle cx="464" cy="603" r="3"/><circle cx="557" cy="548" r="3"/><circle cx="649" cy="442" r="3"/><circle cx="743" cy="434" r="3"/><circle cx="836" cy="427" r="3"/><circle cx="927" cy="427" r="3"/></g>

      <use href="#cube" x="432" y="262" width="64" height="64"/>
      <g transform="translate(460,298)"><path d="M-8 10 Q-12 -6 0 -16 Q12 -6 8 10Z" fill="#b3312a"/><text x="0" y="5" text-anchor="middle" font-family="Oswald,sans-serif" font-size="14" fill="#fff">$</text></g>

      <use href="#cube" x="525" y="232" width="64" height="64"/>
      <g transform="translate(553,268)"><path d="M-18 -8 Q0 -20 18 -8" fill="none" stroke="#b3312a" stroke-width="5" stroke-linecap="round"/><path d="M-8 2 L0 -6 L8 2 L8 12 L-8 12Z" fill="#b3312a"/></g>

      <use href="#cube" x="617" y="190" width="64" height="64"/>
      <g transform="translate(645,226)"><circle r="15" fill="#b3312a"/><path d="M-9 -2 L0 -9 L9 -2 L4 8 L-4 8Z" fill="#fff"/></g>

      <use href="#cube" x="711" y="168" width="64" height="64"/>
      <g transform="translate(739,204)"><path d="M-14 -14 L14 -14 L14 0 Q14 12 0 18 Q-14 12 -14 0Z" fill="#b3312a"/><text x="0" y="6" text-anchor="middle" font-family="Oswald,sans-serif" font-size="17" fill="#fff">$</text></g>

      <use href="#cube" x="804" y="116" width="64" height="64"/>
      <g transform="translate(832,152)"><path d="M-6 -14 L6 -14 L3 -8 Q16 0 12 12 L-12 12 Q-16 0 -3 -8Z" fill="#b3312a"/><text x="0" y="9" text-anchor="middle" font-family="Oswald,sans-serif" font-size="15" fill="#fff">$</text></g>

      <use href="#cube" x="895" y="62" width="64" height="64"/>
      <path transform="translate(923,98)" d="M0 -16 L4.7 -5 L16 -5 L7 2 L10 14 L0 7 L-10 14 L-7 2 L-16 -5 L-4.7 -5Z" fill="#b3312a"/>

      <use href="#cube" x="985" y="43" width="64" height="64"/>
      <g transform="translate(1013,79)"><circle cy="-6" r="8" fill="none" stroke="#b3312a" stroke-width="3"/><path d="M-18 6 Q-4 16 18 4 L18 12 Q-2 20 -18 12Z" fill="#b3312a"/></g>
    </svg>

    <div class="step-label" style="left:464px;top:343px">Wealth<br>Management</div>
    <div class="step-label" style="left:557px;top:313px">Estate<br>Strategy</div>
    <div class="step-label" style="left:649px;top:282px">Cash<br>Management</div>
    <div class="step-label" style="left:743px;top:248px">Risk<br>Management</div>
    <div class="step-label" style="left:836px;top:204px">Tax<br>Strategy</div>
    <div class="step-label" style="left:927px;top:154px">Value Added<br>Services</div>
    <div class="step-label" style="left:1017px;top:127px">Philanthropy</div>

    <div class="headline">WE HELP YOU<br>ACHIEVE IT!!...</div>
    <div class="method-title">BRIGHT PATH METHOD</div>
    <div class="bottom-band"></div>
  </div>
</div>
</body>
</html>
```